Brochure Design Oakridge Capital Partners

Create a brochure, which sells my business. Utilise the website www.oakridgecapitalpartners.example for the details that need to go into the brochure. I would like 2 designs, one for a 4 page brochure and the other for a two page brochure (focus firstly on the 4 page).

The focus points are our 4 year rent guarantee and also out pitch that we are invested with them. Please see the website.

Need to focus on the main points as per the website, can use text from the website and the graphics where suitable.

On the 4 page brochure, first 3 pages to be info as per the website. On the 4 page of the brochure I would like the information included on the final 2 pages of the attached document (the investment property example). Please shrink this down, you do not need to include all the wording more so the figures.

The colours of the brochure to be blue, white and black

Target Market(s)

Property Investors

Industry/Entity Type

Business

Colors
0355a3
ffffff

Requirements
Must have
• Must have the main info on the website, (4 year rent guarantee) 'We are invested with you'
Nice to have
• Professional look

```html
<!DOCTYPE html>
<html lang="en">
<head>
<meta charset="utf-8">
<title>Oakridge Capital Partners – Brochure</title>
<link href="https://fonts.googleapis.com/css2?family=Cinzel:wght@400;600;700&family=Open+Sans:wght@400;600;700&display=swap" rel="stylesheet">
<style>
  :root{
    --navy:#0d2f5c;
    --blue:#0355a3;
    --ink:#1c1c1c;
    --black:#0a0a0a;
    --white:#ffffff;
    --red:#e63a30;
    --gold:#c9a43a;
    --stage:#e9eaec;
    --body:#3a3f47;
  }
  *{box-sizing:border-box;margin:0;padding:0}
  html,body{width:1200px;height:1200px;overflow:hidden;background:var(--stage);font-family:"Open Sans",Arial,sans-serif}
  .stage{position:relative;width:1200px;height:1200px}
  .page{position:absolute;top:337px;width:372px;height:526px;background:var(--white);overflow:hidden;box-shadow:0 6px 18px rgba(0,0,0,.18)}
  .cover{left:24px;background:var(--black)}
  .page-two{left:432px}
  .page-three{left:804px;border-left:1px solid #dcdfe4}

  /* cover */
  .cover-head{position:absolute;top:0;left:0;right:0;height:108px;background:var(--black);display:flex;align-items:center;justify-content:center;gap:10px}
  .cover-head .mark{width:14px;height:14px;background:var(--blue)}
  .cover-head .name{font-family:"Open Sans",sans-serif;font-weight:700;font-size:17px;color:var(--white);letter-spacing:.5px}
  .cover-photo{position:absolute;top:108px;left:0;right:0;height:262px;background:linear-gradient(160deg,#34445a 0%,#1f2b3b 55%,#0f151e 100%)}
  .cover-badge{position:absolute;top:300px;left:280px;width:52px;height:52px;border-radius:50%;background:radial-gradient(circle at 40% 35%,#e7c766,var(--gold) 60%,#8f7224)}
  .cover-title{position:absolute;top:388px;left:0;right:0;text-align:center;font-family:"Cinzel",serif;font-weight:600;color:var(--white);font-size:25px;line-height:1.15;letter-spacing:1px}
  .cover-url{position:absolute;top:466px;left:0;right:0;text-align:center;color:var(--blue);font-size:8.5px;letter-spacing:1px}

  /* page two */
  .service-panel{position:absolute;top:0;left:0;width:246px;height:300px;background:var(--navy);color:var(--white);padding:20px 18px;font-size:6.6px;line-height:1.5}
  .service-panel h2{font-size:7.6px;font-weight:700;margin-bottom:5px;letter-spacing:.2px}
  .service-panel h3{font-size:7.4px;font-weight:700;margin:6px 0 3px}
  .service-panel p{margin-bottom:5px}
  .service-panel ol{margin:4px 0 0 14px}
  .service-panel li{margin-bottom:2px}
  .service-wheel{position:absolute;top:28px;left:252px;width:112px;height:112px}
  .service-copy{position:absolute;top:158px;left:256px;width:104px;font-size:6.3px;line-height:1.5;color:var(--body)}
  .service-copy p{margin-bottom:6px}
  .houses{position:absolute;top:338px;left:26px;width:190px;height:110px;background:linear-gradient(90deg,#9f98d8 0%,#5a52c0 55%,#2e2aa3 100%);border-radius:2px}
  .contact{position:absolute;top:440px;left:236px;color:var(--navy)}
  .contact .url{font-size:6.8px}
  .contact .phone{font-size:11px;margin-top:4px;font-weight:600}
  .footer{position:absolute;bottom:18px;display:flex;align-items:center;gap:8px;font-size:8px;color:var(--navy)}
  .footer .num{background:var(--navy);color:var(--white);width:18px;height:16px;display:flex;align-items:center;justify-content:center;font-size:8px}
  .page-two .footer{left:0}
  .page-three .footer{right:0;flex-direction:row-reverse}

  /* page three */
  .growth{position:absolute;top:24px;left:26px;right:24px}
  .growth h1{font-family:"Cinzel",serif;font-weight:600;color:var(--navy);font-size:17px;letter-spacing:.5px}
  .growth .intro{font-size:6.2px;line-height:1.5;color:var(--body);margin-top:6px}
  .growth h4{font-family:"Cinzel",serif;font-weight:600;color:var(--blue);font-size:9px;margin-top:8px}
  .chart{display:block;margin-top:4px}
  .projection{width:100%;border-collapse:collapse;font-size:6.4px;color:var(--body);margin-top:4px}
  .projection th{background:var(--navy);color:var(--white);font-weight:600;padding:3px 4px;text-align:center}
  .projection td{padding:3px 4px;text-align:center;border-bottom:1px solid #cfd5de}
  .projection td:first-child{text-align:left}
  .summary{font-size:6.3px;line-height:1.5;color:var(--body);margin-top:8px}
  .summary p{margin-bottom:5px}
  .note{font-size:4.8px;line-height:1.45;color:#6b7079;margin-top:4px}
</style>
</head>
<body>
<div class="stage">

  <section class="page cover">
    <div class="cover-head">
      <span class="mark"></span>
      <span class="name">Oakridge Capital Partners</span>
    </div>
    <div class="cover-photo" role="img" aria-label="Photo of a businessman holding a city skyline with a rising growth arrow"></div>
    <div class="cover-badge" role="img" aria-label="Rent guarantee seal"></div>
    <h1 class="cover-title">We are invested<br>with you</h1>
    <div class="cover-url">www.oakridgecapitalpartners.example</div>
  </section>

  <section class="page page-two">
    <div class="service-panel">
      <h2>WE PROVIDE A 360 DEGREE SERVICE</h2>
      <p>At Oakridge Capital Partners, we provide the full solution to your investment property needs. We take our clients from start to the end of their investment circle, ready to go around for the second time.</p>
      <p>We have not only assisted first time investors, but also established property investors with sizable portfolios who have seen the value in the service we were providing.</p>
      <h3>What does the 360 degree service mean to you?</h3>
      <p>First and foremost it means you can stop stressing, sit back and relax as we research both your circumstances and the property market to find you the property which best suits your needs.</p>
      <p>Our 360 Degree service includes the following:</p>
      <ol>
        <li>Assess Finance Capacity</li>
        <li>Establish Property Goals</li>
        <li>Evaluate Property Strategy</li>
        <li>Identify Market Hot Spots</li>
        <li>Provide Suitable Property</li>
        <li>Purchase</li>
        <li>Rent and Manage</li>
      </ol>
    </div>

    <svg class="service-wheel" viewBox="0 0 112 112" role="img" aria-label="360 degree service cycle">
      <circle cx="56" cy="56" r="40" fill="none" stroke="#0d2f5c" stroke-width="1"/>
      <g fill="#0d2f5c">
        <circle cx="56" cy="14" r="11"/>
        <circle cx="88.8" cy="29.8" r="11"/>
        <circle cx="96.9" cy="65.3" r="11"/>
        <circle cx="74.2" cy="93.8" r="11"/>
        <circle cx="37.8" cy="93.8" r="11"/>
        <circle cx="15.1" cy="65.3" r="11"/>
        <circle cx="23.2" cy="29.8" r="11"/>
      </g>
      <g fill="#fff" font-family="Open Sans, sans-serif" font-size="3.6" text-anchor="middle">
        <text x="56" y="15">Finance</text>
        <text x="88.8" y="31">Goals</text>
        <text x="96.9" y="66.5">Strategy</text>
        <text x="74.2" y="95">Hot Spots</text>
        <text x="37.8" y="95">Property</text>
        <text x="15.1" y="66.5">Purchase</text>
        <text x="23.2" y="31">Manage</text>
      </g>
      <circle cx="56" cy="56" r="20" fill="#0a0a0a"/>
      <text x="56" y="55" fill="#fff" font-family="Open Sans, sans-serif" font-size="8" font-weight="700" text-anchor="middle">360°</text>
      <text x="56" y="64" fill="#fff" font-family="Open Sans, sans-serif" font-size="6" text-anchor="middle">service</text>
    </svg>

    <div class="service-copy">
      <p>At Oakridge Capital Partners, we ensure all our investment property experts are here to provide you the guidance and expertise to secure your first investment. They are there as a mentor to focus you into building a portfolio which can really make a difference to both you and your families' life. We are always looking two steps ahead. When we are helping you with your first investment, we are also laying the foundation for your second and third.</p>
      <p>Ultimately Oakridge Capital Partners is looking to assist you reach your financial goals with as little stress as possible. We will be there every step of the way to provide you the support and guidance you require.</p>
      <p>If you would like to know how we can assist you, please contact us today and set up an appointment with one of our mobile property advisors.</p>
    </div>

    <div class="houses" role="img" aria-label="Illustration of a row of rising purple houses"></div>

    <div class="contact">
      <div class="url">www.oakridgecapitalpartners.example</div>
      <div class="phone">1300 555 014</div>
    </div>

    <div class="footer"><span class="num">2</span><span>Oakridge Capital Partners</span></div>
  </section>

  <section class="page page-three">
    <div class="growth">
      <h1>Growth Projection</h1>
      <p class="intro">Whilst capital growth is never a guarantee in the short term, in the long term history has shown one undeniable fact, property prices in Australian capital cities and major metropolitan areas increase in value. Below is an example of what a property purchased today in South East Queensland can be expected to make over the next 20 years based on a 6% growth rate. This is a rate which many experts believe is likely in the region, with some predicting even greater growth.</p>
      <h4>6% Growth per annum</h4>

      <svg class="chart" width="322" height="150" viewBox="0 0 322 150" role="img" aria-label="Stacked bar chart of debt and capital gain over 20 years">
        <g font-family="Open Sans, sans-serif" font-size="4.6" fill="#6b7079" text-anchor="end">
          <text x="30" y="132">0</text>
          <text x="30" y="110.3">250,000</text>
          <text x="30" y="88.7">500,000</text>
          <text x="30" y="67">750,000</text>
          <text x="30" y="45.3">1,000,000</text>
          <text x="30" y="23.7">1,250,000</text>
          <text x="30" y="2">1,500,000</text>
        </g>
        <line x1="34" y1="130" x2="270" y2="130" stroke="#c8ccd3" stroke-width=".6"/>
        <!-- debt 428k = 37.1 ; scale 130 per 1.5M -->
        <rect x="44" y="92.9" width="32" height="37.1" fill="#e63a30"/>
        <rect x="90" y="92.9" width="32" height="37.1" fill="#e63a30"/>
        <rect x="90" y="80.4" width="32" height="12.5" fill="#0d2f5c"/>
        <rect x="136" y="92.9" width="32" height="37.1" fill="#e63a30"/>
        <rect x="136" y="63.6" width="32" height="29.3" fill="#0d2f5c"/>
        <rect x="182" y="92.9" width="32" height="37.1" fill="#e63a30"/>
        <rect x="182" y="41.1" width="32" height="51.8" fill="#0d2f5c"/>
        <rect x="228" y="92.9" width="32" height="37.1" fill="#e63a30"/>
        <rect x="228" y="11" width="32" height="81.9" fill="#0d2f5c"/>
        <g font-family="Open Sans, sans-serif" font-size="4.8" fill="#6b7079" text-anchor="middle">
          <text x="60" y="139">Current</text>
          <text x="106" y="139">5 years</text>
          <text x="152" y="139">10 years</text>
          <text x="198" y="139">15 years</text>
          <text x="244" y="139">20 years</text>
        </g>
        <rect x="280" y="60" width="6" height="6" fill="#e63a30"/>
        <text x="290" y="65.5" font-family="Open Sans, sans-serif" font-size="6" fill="#3a3f47">Debt</text>
        <rect x="280" y="76" width="6" height="6" fill="#0d2f5c"/>
        <text x="290" y="81.5" font-family="Open Sans, sans-serif" font-size="6" fill="#3a3f47">Capital</text>
        <text x="290" y="89" font-family="Open Sans, sans-serif" font-size="6" fill="#3a3f47">Gain</text>
      </svg>

      <table class="projection">
        <thead>
          <tr><th></th><th>Current</th><th>5 years</th><th>10 years</th><th>15 years</th><th>20 years</th></tr>
        </thead>
        <tbody>
          <tr><td>Property Value</td><td>$428,000</td><td>$572,790</td><td>$766,482</td><td>$1,025,726</td><td>$1,372,653</td></tr>
          <tr><td>Capital Gain</td><td>0</td><td>$144,790</td><td>$338,790</td><td>$597,726</td><td>$944,653</td></tr>
        </tbody>
      </table>

      <div class="summary">
        <p>Based off the above table you can easily identify the reason so many Australia's have a love for property. Gaining $944,653 profit in 20 years for doing very little and utilising the banks to your advantage. Also, this is not taking into account the rental profit you will make, especially as time increases and your rent goes up.</p>
        <p>Now imagine you purchased 2 or 3 or even 5. It is possible and many people are limited only by their ability to make a decision.</p>
        <p>For further details on what your potential is and how we can help you achieve it, please contact Oakridge Capital Partners to speak with one of our expert property consultants.</p>
      </div>
      <p class="note">NOTE: The above is an example only and may not depict exact figures, however it may be used as a general guide. Interest at 4.2% on $428,000 interest only loan. Depreciation is based on a report of a similar property and may not reflect exact write down, although it will be within a few hundred dollars. Tax deductions based off a single income of $90,000.</p>
    </div>

    <div class="footer"><span class="num">3</span><span>Oakridge Capital Partners</span></div>
  </section>

</div>
</body>
</html>
```